Flyer-Design für Beratungsunternehmen
Vielen Dank für die professionelle und überdurchschnittliche Unterstützung
Zielgruppe
Supervision, Coaching, Beratung
Plus digitale Beratung via App, sonstiger moderner Medien
für Organisationen, Firmen, Institutionen, Privatpersonen
Aufgabenstellung
Kreatives Design, modern, hochwertig
symphatisch, vertrauensvoll, transparent, ansprechend
Texte, Inhalte und Bilder siehe download
Sehr wichtig corporate design laut homepage www.reflexionamufer.de

```html
<!DOCTYPE html>
<html lang="de">
<head>
<meta charset="utf-8">
<title>Reflexion am Ufer – Flyer</title>
<link rel="stylesheet" href="https://fonts.googleapis.com/css2?family=Didact+Gothic&family=Oswald:wght@500;600&display=swap">
<style>
  :root {
    --green: #8dc21f;
    --green-light: #c9e39a;
    --orange: #e98b23;
    --ink: #1d1d1b;
    --white: #ffffff;
    --photo-left-a: #f4f7fb;
    --photo-left-b: #6f93bf;
    --photo-left-c: #f2c6c8;
    --photo-right-a: #e9ecee;
    --photo-right-b: #c7cdd2;
  }
  * { margin: 0; padding: 0; box-sizing: border-box; }
  html, body { width: 1200px; height: 600px; overflow: hidden; background: var(--white); }
  .flyer { position: relative; width: 1200px; height: 600px; overflow: hidden; font-family: "Didact Gothic", sans-serif; color: var(--white); }

  .photo { position: absolute; top: 0; height: 380px; }
  .photo--motion { left: 0; width: 600px;
    background:
      radial-gradient(ellipse 220px 120px at 150px 90px, var(--photo-left-c), transparent 70%),
      linear-gradient(160deg, var(--photo-left-a) 0%, #e3ebf4 40%, var(--photo-left-b) 75%, #3e5f8c 100%); }
  .photo--portrait { left: 600px; width: 600px;
    background: linear-gradient(90deg, var(--photo-right-b) 0%, var(--photo-right-a) 45%, #f6f7f8 100%); }

  .band { position: absolute; inset: 0; width: 1200px; height: 600px; }

  .brand { position: absolute; display: flex; align-items: center; gap: 8px;
    font-family: "Didact Gothic", sans-serif; font-size: 21px; letter-spacing: 0.5px; color: var(--ink); white-space: nowrap; }
  .brand__mark { width: 14px; height: 14px; background: var(--green); }
  .brand--left { left: 365px; top: 102px; }
  .brand--right { left: 975px; top: 96px; }

  .badge { position: absolute; left: 940px; top: 270px; width: 146px; height: 146px; border-radius: 50%;
    background: var(--orange); border: 5px solid var(--green-light);
    display: flex; align-items: center; justify-content: center; }
  .badge__text { transform: rotate(-9deg); font-family: "Oswald", sans-serif; font-weight: 600;
    font-size: 19px; line-height: 1.15; text-align: center; color: var(--white); text-transform: uppercase; }

  .quote { position: absolute; left: 47px; top: 412px; font-size: 28.5px; line-height: 36.5px;
    letter-spacing: -0.2px; text-transform: uppercase; }
  .quote__author { position: absolute; left: 47px; width: 418px; top: 538px; text-align: right; font-size: 11.5px; }

  .contact-person { position: absolute; left: 666px; top: 458px; }
  .contact-person__name { font-family: "Oswald", sans-serif; font-weight: 500; font-size: 16px; letter-spacing: 0.3px; text-transform: uppercase; }
  .contact-person__address { margin-top: 18px; font-size: 14.5px; line-height: 19.5px; font-style: normal; }

  .contact-channels { position: absolute; left: 880px; top: 460px; font-size: 14.5px; line-height: 19.5px; }
  .contact-channels dt { float: left; width: 60px; clear: left; }
  .contact-channels dd { margin-left: 60px; }
  .contact-channels .web-label { margin-top: 19.5px; }
  .contact-channels .web-url { font-weight: bold; font-family: "Didact Gothic", sans-serif; font-size: 15px; -webkit-text-stroke: 0.5px var(--white); }
</style>
</head>
<body>
<main class="flyer">
  <div class="photo photo--motion" role="img" aria-label="Foto: Lichtspuren einer schnellen Fahrt durch einen hellen Tunnel"></div>
  <div class="photo photo--portrait" role="img" aria-label="Porträtfoto der Beraterin vor heller Bürokulisse"></div>

  <svg class="band" viewBox="0 0 1200 600" aria-hidden="true">
    <path d="M600 345 Q900 300 1200 285 L1200 330 Q900 330 600 360 Z" fill="#ffffff" opacity="0.45"/>
    <path d="M0 358 Q300 380 600 360 Q900 332 1200 326 L1200 600 L0 600 Z" fill="#ffffff"/>
    <path d="M0 364 Q300 386 600 366 Q900 338 1200 332 L1200 600 L0 600 Z" fill="var(--green)"/>
  </svg>

  <div class="brand brand--left"><span class="brand__mark"></span>REFLEXION AM UFER</div>
  <div class="brand brand--right"><span class="brand__mark"></span>REFLEXION AM UFER</div>

  <div class="badge"><p class="badge__text">Ich freue<br>mich auf<br>Sie!</p></div>

  <blockquote class="quote">„Es ist nicht zu wenig Zeit<br>die wir haben, sondern es ist zu<br>viel Zeit, die wir nicht nutzen.“</blockquote>
  <p class="quote__author">Lucius Aemilius Varro – Philosoph</p>

  <section class="contact-person">
    <h2 class="contact-person__name">Lena Burkhard</h2>
    <address class="contact-person__address">Uferweg 12<br>35578 Wetzlar<br>an der Lahn</address>
  </section>

  <dl class="contact-channels">
    <dt>Telefon:</dt><dd>+49 (0)170 555 01 23</dd>
    <dt>E-Mail:</dt><dd>info@reflexionamufer.de</dd>
    <dt class="web-label">Web:</dt><dd class="web-label">&nbsp;</dd>
    <dd class="web-url" style="margin-left:0">www.reflexionamufer.de</dd>
  </dl>
</main>
</body>
</html>
```